Upgrade Wordpress Website

We have an existing website www.brindlecovetrust.org.au - we require improved shop, improved donation visibility and interactive forms for sponsorship

```html
<!DOCTYPE html>
<html lang="en">
<head>
<meta charset="utf-8">
<title>Brindle Cove Equine Sanctuary</title>
<link rel="stylesheet" href="https://fonts.googleapis.com/css2?family=Libre+Baskerville:wght@400;700&family=Roboto:wght@400;500;700&display=swap">
<style>
:root{
  --orange:#f5842b;
  --orange-dark:#e8721a;
  --ink:#1d1d1d;
  --text:#3a3a3a;
  --muted:#6b6b6b;
  --grey-bg:#ececec;
  --panel:#efefef;
  --white:#ffffff;
  --black:#000000;
  --brand-red:#d8452b;
}
*{margin:0;padding:0;box-sizing:border-box}
html,body{width:1200px;height:4275px;overflow:hidden}
body{position:relative;background:var(--white);font-family:'Roboto',sans-serif;color:var(--text)}
.abs{position:absolute}
.serif{font-family:'Libre Baskerville',serif}
.icon-dot{position:absolute;width:36px;height:36px;border-radius:50%;background:var(--orange);display:flex;align-items:center;justify-content:center}
.btn{position:absolute;background:var(--orange);color:var(--white);font-family:'Libre Baskerville',serif;font-weight:700;font-size:15px;display:flex;align-items:center;justify-content:center;border-radius:4px;box-shadow:0 4px 8px rgba(0,0,0,.15);letter-spacing:.3px}
.photo{position:absolute;overflow:hidden}
.play{position:absolute;width:56px;height:56px;border-radius:50%;background:var(--orange);display:flex;align-items:center;justify-content:center;transform:translate(-50%,-50%)}
.section-title{position:absolute;left:0;width:1200px;text-align:center;font-family:'Libre Baskerville',serif;font-weight:700;font-size:28px;color:var(--ink)}
.brand{left:111px;top:24px;font-family:'Libre Baskerville',serif;color:var(--brand-red);font-size:18px;line-height:1;white-space:nowrap}
.brand small{display:block;font-size:10px;margin-top:6px;color:var(--brand-red)}
.brand-mark{left:244px;top:22px;width:16px;height:54px;background:var(--orange)}
.contact-line{font-size:15px;color:var(--ink);line-height:21px}
.topline{left:0;top:94px;width:1200px;height:1px;background:#ddd}
.nav a{position:absolute;top:121px;font-size:15px;color:var(--ink);text-decoration:none}
.nav a.active{font-weight:700}
.card{position:absolute;background:var(--panel)}
.card .date{position:absolute;left:28px;font-family:'Libre Baskerville',serif;font-size:16px;color:var(--ink);display:flex;align-items:center;gap:10px}
.card .title{position:absolute;left:28px;font-family:'Libre Baskerville',serif;font-size:17px;color:var(--orange);white-space:nowrap}
.field{position:absolute;background:var(--white);border:1px solid #ddd;font-size:12px;color:#777;display:flex;align-items:center;padding-left:20px;gap:10px}
.foot-title{position:absolute;font-family:'Libre Baskerville',serif;font-weight:700;font-size:15px;color:var(--white)}
.foot-list{position:absolute;list-style:none;color:var(--white)}
.foot-list li{height:30px;font-size:15px}
.foot-list.small li{font-size:13px}
.social{position:absolute;top:4060px;width:30px;height:30px;border-radius:50%;background:var(--orange)}
.pay{position:absolute;top:4226px;width:30px;height:20px;border-radius:3px}
</style>
</head>
<body>

<div class="abs brand">Brindle Cove<small>Equine Sanctuary</small></div>
<div class="abs brand-mark"></div>

<div class="icon-dot" style="left:337px;top:32px"><svg width="16" height="18" viewBox="0 0 16 18"><path d="M8 0a6 6 0 0 0-6 6c0 5 6 12 6 12s6-7 6-12a6 6 0 0 0-6-6zm0 8.5A2.5 2.5 0 1 1 8 3.5a2.5 2.5 0 0 1 0 5z" fill="#fff"/></svg></div>
<div class="abs contact-line" style="left:383px;top:30px">Brindle Cove Equine<br>Sanctuary Ridgeway VIC 3391</div>

<div class="icon-dot" style="left:629px;top:32px"><svg width="16" height="12" viewBox="0 0 16 12"><rect width="16" height="12" rx="1.5" fill="#fff"/><path d="M1 1l7 6 7-6" stroke="#f5842b" stroke-width="1.6" fill="none"/></svg></div>
<div class="abs contact-line" style="left:680px;top:40px">admin@brindlecovetrust.org.au</div>

<div class="icon-dot" style="left:942px;top:32px"><svg width="16" height="16" viewBox="0 0 16 16"><path d="M3.5 1l3 3-1.8 2.2a10 10 0 0 0 5.1 5.1L12 9.5l3 3-2 2.5C6.5 15 1 9.5 1 3z" fill="#fff"/></svg></div>
<div class="abs contact-line" style="left:992px;top:40px">0400 512 688</div>

<div class="abs topline"></div>

<nav class="nav">
  <a class="active" style="left:108px">HOME</a>
  <a style="left:181px">Horses For Adoption</a>
  <a style="left:352px">For sponsorship</a>
  <a style="left:493px">Shop</a>
  <a style="left:557px">Lease Adopted</a>
  <a style="left:690px">Sponsored</a>
  <a style="left:793px">Rip</a>
  <a style="left:845px">Contact</a>
</nav>
<div class="btn" style="left:936px;top:109px;width:152px;height:46px;font-size:14px">DONATE NOW</div>

<div class="photo" role="img" aria-label="Paint horse standing in a golden grass field with forest behind" style="left:0;top:175px;width:1200px;height:700px;background:linear-gradient(180deg,#3c4a3a 0%,#5b6347 35%,#8a7a4c 65%,#a88a50 100%)"></div>
<div class="abs serif" style="left:111px;top:372px;font-size:42px;font-weight:700;line-height:56px;color:var(--white)">WELCOME TO<br>BRINDLE COVE</div>
<div class="abs" style="left:113px;top:484px;font-size:15px;line-height:29px;color:var(--white)">Brindle Cove Equine Sanctuary (BCES) was<br>founded by passionate animal lovers</div>
<div class="btn" style="left:111px;top:555px;width:167px;height:52px">GET STARTED</div>
<div class="abs" style="left:26px;top:455px;width:46px;height:46px;border-radius:50%;background:var(--orange)"><svg width="46" height="46"><path d="M26 17l-6 6 6 6" stroke="#fff" stroke-width="2.5" fill="none"/></svg></div>
<div class="abs" style="left:1127px;top:455px;width:46px;height:46px;border-radius:50%;background:var(--orange)"><svg width="46" height="46"><path d="M20 17l6 6-6 6" stroke="#fff" stroke-width="2.5" fill="none"/></svg></div>
<svg class="abs" style="left:0;top:730px" width="1200" height="160" viewBox="0 0 1200 160">
  <path d="M0 80 C220 -10 420 40 620 80 S960 160 1200 60 L1200 160 L0 160 Z" fill="#fff"/>
  <path d="M0 80 C220 -10 420 40 620 80 S960 160 1200 60" stroke="#f5842b" stroke-width="7" fill="none"/>
</svg>

<div class="abs" style="left:111px;top:933px;width:393px;height:393px;border-radius:50%;border:6px solid var(--orange);overflow:hidden">
  <div role="img" aria-label="Woman resting her head against a grey horse at sunset" style="width:100%;height:100%;background:radial-gradient(circle at 70% 30%,#f3b46a 0%,#c1783a 45%,#6e4529 100%)"></div>
</div>
<div class="abs serif" style="left:602px;top:968px;font-size:27px;font-weight:700;color:var(--ink)">ABOUT BRINDLE COVE</div>
<p class="abs" style="left:600px;top:1015px;width:490px;font-size:14.5px;line-height:30px;text-align:justify;color:var(--text)">Brindle Cove Equine Sanctuary (BCES) was founded by passionate animal lovers and advocates in 2014, in response to an ever-increasing number of horses passing through the saleyards, and into the hands of knackeries. The name was selected to pay homage to the brilliant protective work done by the Ocean Guardians, and to reflect our mission of providing sanctuary and solace to unwanted, injured, and otherwise vulnerable horses</p>
<div class="btn" style="left:600px;top:1236px;width:167px;height:50px">READ MORE</div>
<div class="btn" style="left:782px;top:1236px;width:176px;height:50px">SPONSORSHIP</div>

<div class="abs" style="left:0;top:1413px;width:1200px;height:946px;background:linear-gradient(180deg,#f28a3a 0%,#f5842b 50%,#f28a3a 100%)"></div>
<div class="section-title" style="top:1480px;color:var(--white)">MEDIA</div>
<div class="photo" role="img" aria-label="Two ponies touching noses over a fence" style="left:111px;top:1557px;width:977px;height:433px;border-radius:8px;background:linear-gradient(110deg,#6a4a2c 0%,#8c5c34 40%,#6f7a3e 70%,#3e4a2c 100%)"></div>
<div class="play" style="left:600px;top:1775px"><svg width="20" height="22"><path d="M3 2l15 9-15 9z" fill="#fff"/></svg></div>

<div class="photo" role="img" aria-label="Mare with foal" style="left:111px;top:2007px;width:234px;height:231px;background:linear-gradient(135deg,#8a6a4c,#4a3a2e)"></div>
<div class="photo" style="left:360px;top:2007px;width:232px;height:231px;background:var(--white);padding:9px"><div role="img" aria-label="Chestnut horse head close-up" style="width:100%;height:100%;background:linear-gradient(135deg,#c47a3e,#5a3a24)"></div></div>
<div class="photo" role="img" aria-label="Smiling woman hugging a horse" style="left:607px;top:2007px;width:234px;height:231px;background:linear-gradient(135deg,#6a3a2a,#b08060)"></div>
<div class="photo" role="img" aria-label="Pony being fed at a fence" style="left:855px;top:2007px;width:233px;height:231px;background:linear-gradient(135deg,#b07a4a,#5a4a3a)"></div>
<div class="play" style="left:228px;top:2122px"><svg width="20" height="22"><path d="M3 2l15 9-15 9z" fill="#fff"/></svg></div>
<div class="play" style="left:476px;top:2122px"><svg width="20" height="22"><path d="M3 2l15 9-15 9z" fill="#fff"/></svg></div>
<div class="play" style="left:724px;top:2122px"><svg width="20" height="22"><path d="M3 2l15 9-15 9z" fill="#fff"/></svg></div>
<div class="play" style="left:971px;top:2122px"><svg width="20" height="22"><path d="M3 2l15 9-15 9z" fill="#fff"/></svg></div>

<div class="section-title" style="top:2440px">LATEST NEWS</div>

<div class="card" style="left:111px;top:2540px;width:647px;height:287px;background:var(--white);box-shadow:0 2px 10px rgba(0,0,0,.1)">
  <div class="photo" role="img" aria-label="Horses grazing on hay" style="left:0;top:0;width:315px;height:287px;background:linear-gradient(135deg,#7a8a4a,#4a3a2a)"></div>
  <div class="date" style="left:343px;top:34px"><svg width="16" height="16"><rect x="1" y="3" width="14" height="12" fill="#222"/><rect x="3" y="0" width="2" height="4" fill="#222"/><rect x="11" y="0" width="2" height="4" fill="#222"/></svg>Dec16 ,2021</div>
  <div class="title" style="left:343px;top:70px;font-size:18px;line-height:28px">Calendars Are Still<br>Available But Selling Fast!</div>
  <p class="abs" style="left:343px;top:134px;width:280px;font-size:14px;line-height:28px">Sed ut perspiciatis unde omnis iste natus error sit doloremque laudantium, totam rem aperiam, eaque ipsa quae</p>
  <div class="abs serif" style="left:343px;top:228px;font-size:14px;color:var(--orange)">Read&nbsp; More »</div>
</div>

<div class="card" style="left:773px;top:2540px;width:315px;height:288px">
  <div class="photo" role="img" aria-label="Horses drinking from a trough" style="left:0;top:0;width:315px;height:206px;background:linear-gradient(135deg,#9a6a3a,#3a2a20)"></div>
  <div class="date" style="left:28px;top:225px"><svg width="16" height="16"><rect x="1" y="3" width="14" height="12" fill="#222"/><rect x="3" y="0" width="2" height="4" fill="#222"/><rect x="11" y="0" width="2" height="4" fill="#222"/></svg>Dec 29,2021</div>
  <div class="title" style="top:253px">Nurse BCES Bob</div>
</div>

<div class="card" style="left:111px;top:2842px;width:315px;height:290px">
  <div class="photo" role="img" aria-label="Bay horse grazing in a paddock" style="left:0;top:0;width:315px;height:206px;background:linear-gradient(135deg,#6a8a3a,#7a4a2a)"></div>
  <div class="date" style="top:225px"><svg width="16" height="16"><rect x="1" y="3" width="14" height="12" fill="#222"/><rect x="3" y="0" width="2" height="4" fill="#222"/><rect x="11" y="0" width="2" height="4" fill="#222"/></svg>Dec 29,2021</div>
  <div class="title" style="top:253px">BCES Wilbur 35 yrs young</div>
</div>
<div class="card" style="left:443px;top:2842px;width:314px;height:290px">
  <div class="photo" role="img" aria-label="Herd of horses in a field" style="left:0;top:0;width:314px;height:206px;background:linear-gradient(135deg,#5a5a3a,#3a2a20)"></div>
  <div class="date" style="top:225px"><svg width="16" height="16"><rect x="1" y="3" width="14" height="12" fill="#222"/><rect x="3" y="0" width="2" height="4" fill="#222"/><rect x="11" y="0" width="2" height="4" fill="#222"/></svg>Dec 29,2021</div>
  <div class="title" style="top:253px">148 years of Horse</div>
</div>
<div class="card" style="left:773px;top:2844px;width:315px;height:290px">
  <div class="photo" role="img" aria-label="Group of ponies in a sandy yard" style="left:0;top:0;width:315px;height:206px;background:linear-gradient(135deg,#a88a6a,#5a3a24)"></div>
  <div class="date" style="top:225px"><svg width="16" height="16"><rect x="1" y="3" width="14" height="12" fill="#222"/><rect x="3" y="0" width="2" height="4" fill="#222"/><rect x="11" y="0" width="2" height="4" fill="#222"/></svg>Dec 29,2021</div>
  <div class="title" style="top:253px">See our recent Social Posts</div>
</div>

<div class="abs" style="left:0;top:3220px;width:1200px;height:620px;background:var(--grey-bg)"></div>
<div class="section-title" style="top:3302px">CONTACT US</div>
<div class="abs" style="left:163px;top:3412px;font-size:20px;font-weight:700;line-height:30px;color:var(--ink)">Let's Make Somethinkg<br>great Together</div>
<div class="abs" style="left:163px;top:3502px;font-size:14px;line-height:25px;color:var(--muted)">Sed ut perspiciatis unde<br>omnisistenatus error sit voluptatem</div>
<div class="icon-dot" style="left:163px;top:3574px;width:28px;height:28px"><svg width="12" height="14" viewBox="0 0 16 18"><path d="M8 0a6 6 0 0 0-6 6c0 5 6 12 6 12s6-7 6-12a6 6 0 0 0-6-6z" fill="#fff"/></svg></div>
<div class="abs" style="left:207px;top:3566px;font-size:15px;line-height:25px;color:var(--ink)">Brindle Cove Equine<br>Sanctuary Ridgeway VIC 3391</div>
<div class="icon-dot" style="left:163px;top:3616px;width:28px;height:28px"><svg width="12" height="12" viewBox="0 0 16 16"><path d="M3.5 1l3 3-1.8 2.2a10 10 0 0 0 5.1 5.1L12 9.5l3 3-2 2.5C6.5 15 1 9.5 1 3z" fill="#fff"/></svg></div>
<div class="abs" style="left:207px;top:3620px;font-size:15px;color:var(--ink)">0400 512 688</div>
<div class="abs" style="left:163px;top:3670px;width:28px;height:28px;border-radius:50%;border:2px solid var(--orange);display:flex;align-items:center;justify-content:center"><svg width="13" height="10"><rect width="13" height="10" rx="1" fill="#f5842b"/></svg></div>
<div class="abs" style="left:207px;top:3674px;font-size:15px;color:var(--ink)">admin@brindlecovetrust.org.au</div>

<div class="abs serif" style="left:497px;top:3388px;font-size:18px;font-weight:700;color:var(--orange)">GET IN TOUCH</div>
<div class="field" style="left:502px;top:3432px;width:263px;height:48px">👤 Frist Name</div>
<div class="field" style="left:775px;top:3432px;width:261px;height:48px">👤 Last Name</div>
<div class="field" style="left:502px;top:3495px;width:263px;height:48px">✉ Email Address</div>
<div class="field" style="left:775px;top:3495px;width:261px;height:48px">☏ Phone Number</div>
<div class="field" style="left:502px;top:3555px;width:534px;height:65px">💬 Message ......</div>
<div class="btn" style="left:502px;top:3638px;width:121px;height:43px;font-family:'Roboto',sans-serif;font-size:14px;border-radius:8px">SUMBIT</div>

<svg class="abs" style="left:0;top:3700px" width="1200" height="160" viewBox="0 0 1200 160">
  <path d="M0 100 C200 160 420 90 640 60 S1000 30 1200 40 L1200 160 L0 160 Z" fill="#000"/>
  <path d="M0 100 C200 160 420 90 640 60 S1000 30 1200 40" stroke="#f5842b" stroke-width="7" fill="none"/>
</svg>
<div class="abs" style="left:1100px;top:3728px;width:56px;height:56px;border-radius:50%;background:var(--orange);border:3px solid var(--white);display:flex;align-items:center;justify-content:center"><svg width="26" height="22"><path d="M2 2h22v14H10l-6 5v-5H2z" fill="none" stroke="#fff" stroke-width="2"/><circle cx="8" cy="9" r="1.6" fill="#fff"/><circle cx="13" cy="9" r="1.6" fill="#fff"/><circle cx="18" cy="9" r="1.6" fill="#fff"/></svg></div>

<div class="abs" style="left:0;top:3855px;width:1200px;height:420px;background:var(--black)"></div>
<div class="abs serif" style="left:111px;top:3915px;font-size:30px;line-height:36px;color:var(--brand-red)">Brindle<br>Cove</div>
<div class="abs serif" style="left:111px;top:3995px;font-size:14px;color:var(--brand-red)">Equine Sanctuary</div>
<div class="abs" style="left:262px;top:3900px;width:32px;height:118px;background:var(--orange)"></div>

<div class="foot-title" style="left:388px;top:3895px">QUICK MENU</div>
<ul class="foot-list" style="left:390px;top:3928px">
  <li>Home</li><li>Horses For Adoption</li><li>For sponsorship</li><li>Shop</li><li>Lease Adopted</li><li>Sponsored</li><li>Rip</li><li>Contact &amp; Forms</li>
</ul>
<div class="foot-title" style="left:603px;top:3895px">HELP LINKS</div>
<ul class="foot-list small" style="left:604px;top:3930px">
  <li>Terms&amp;condtions</li><li>Privacy Policy</li><li>About Us</li><li>Support</li><li>Media</li>
</ul>
<div class="foot-title" style="left:782px;top:3895px">NEWSLETTER</div>
<div class="abs" style="left:782px;top:3925px;font-size:15px;line-height:30px;color:var(--white)">For news, events and updates, subscribe<br>to our newsletter.</div>
<div class="abs" style="left:782px;top:3992px;width:286px;height:42px;border-radius:21px;background:var(--white);font-size:13px;color:#888;display:flex;align-items:center;padding-left:16px">Enter The Email</div>
<svg class="abs" style="left:1030px;top:4004px" width="18" height="18"><path d="M1 9L17 1 12 17 9 10z" fill="#f5842b"/></svg>
<div class="social" style="left:783px"></div>
<div class="social" style="left:826px"></div>
<div class="social" style="left:868px"></div>
<div class="social" style="left:911px"></div>

<div class="abs" style="left:111px;top:4203px;width:977px;height:1px;background:#444"></div>
<div class="abs" style="left:0;top:4228px;width:1200px;text-align:center;font-size:13px;color:var(--white)">© Copyright 2022&nbsp; brindlecovetrust | All Rights Reserved</div>
<div class="pay" style="left:900px;background:#2b5fb4"></div>
<div class="pay" style="left:936px;background:#1a4fb8"></div>
<div class="pay" style="left:972px;background:#f09a1e"></div>
<div class="pay" style="left:1008px;background:#2e7ec4"></div>

</body>
</html>
```